Accommodation business card design

We need a business card designed for our long-term accommodation business based in Australia. The business card must match the style of the attached letterhead and logo. The same contact details that are on the letterhead will also go on the card except that the card must list the contact details in the following order:phone, email, home address, ABN.

The card will be printed on .76mm white pvc plastic (same as credit cards), printed both sides and will be silver foil stamped on at least one side (preferably 2 sides) The design template is attached, but please go to www.zt.com.au for more specs.

The only other addition the card will be my name: Malcolm Darby

```html
<!DOCTYPE html>
<html lang="en">
<head>
<meta charset="utf-8">
<title>Calder Rooms – Business Card</title>
<link href="https://fonts.googleapis.com/css2?family=Open+Sans:wght@400;600&family=Quicksand:wght@500&display=swap" rel="stylesheet">
<style>
  :root{
    --maroon:#7b1e45;
    --brown:#8c5a48;
    --pink-line:#e6a9c2;
    --trim:#9a9a9a;
    --white:#ffffff;
    --muted:#b88a9c;
  }
  *{margin:0;padding:0;box-sizing:border-box}
  html,body{width:849px;height:1200px;overflow:hidden;background:var(--white)}
  body{position:relative;font-family:"Open Sans",Arial,sans-serif}

  .trim-marks{position:absolute;inset:0;width:849px;height:1200px}
  .card{position:absolute;left:52px;width:745px;height:531px;overflow:hidden}
  .card--front{top:57px;background:var(--white)}
  .card--back{top:645px;background:var(--maroon)}
  .card__art{position:absolute;inset:0;width:745px;height:531px}

  .brand{position:absolute;left:0;right:0;top:150px;display:flex;justify-content:center;align-items:center;gap:18px}
  .brand__dot{width:34px;height:34px;border-radius:50%;background:var(--brown)}
  .brand__name{font-family:"Open Sans",Arial,sans-serif;font-weight:600;color:var(--brown);font-size:52px;line-height:1}
  .holder-name{position:absolute;left:0;right:0;top:262px;text-align:center;font-family:"Quicksand",Arial,sans-serif;
    font-weight:500;font-size:46px;color:var(--maroon);letter-spacing:1px}

  .contact{position:absolute;left:158px;top:168px;list-style:none;color:var(--white);font-size:26px;line-height:1.35}
  .contact li{display:flex;align-items:flex-start;gap:12px;margin-bottom:8px}
  .contact__icon{width:30px;height:30px;flex:none;margin-top:3px}
  .contact__text--abn{padding-left:42px}
  .contact__label{color:var(--muted)}
</style>
</head>
<body>

<svg class="trim-marks" viewBox="0 0 849 1200" aria-hidden="true">
  <g stroke="var(--trim)" stroke-width="1">
    <line x1="52" y1="0" x2="52" y2="40"/><line x1="797" y1="0" x2="797" y2="40"/>
    <line x1="0" y1="57" x2="36" y2="57"/><line x1="813" y1="57" x2="849" y2="57"/>
    <line x1="0" y1="588" x2="36" y2="588"/><line x1="813" y1="588" x2="849" y2="588"/>
    <line x1="0" y1="645" x2="36" y2="645"/><line x1="813" y1="645" x2="849" y2="645"/>
    <line x1="0" y1="1162" x2="36" y2="1162"/><line x1="813" y1="1162" x2="849" y2="1162"/>
    <line x1="52" y1="1178" x2="52" y2="1200"/><line x1="797" y1="1178" x2="797" y2="1200"/>
  </g>
</svg>

<section class="card card--front">
  <svg class="card__art" viewBox="0 0 745 531" aria-hidden="true">
    <rect x="30" y="24" width="685" height="483" rx="34" fill="none" stroke="var(--pink-line)" stroke-width="2"/>
    <path d="M0,355 C200,420 430,430 745,370 L745,531 L0,531 Z" fill="var(--maroon)"/>
    <path d="M0,468 C240,440 500,405 745,392 C500,415 250,448 0,480 Z" fill="var(--white)"/>
  </svg>
  <div class="brand">
    <div class="brand__dot"></div>
    <div class="brand__name">Calder Rooms</div>
  </div>
  <p class="holder-name">Malcolm Darby</p>
</section>

<section class="card card--back">
  <svg class="card__art" viewBox="0 0 745 531" aria-hidden="true">
    <path d="M0,392 C250,398 500,440 745,478 L745,531 L0,531 Z" fill="var(--brown)"/>
    <path d="M0,386 C250,392 500,432 745,470" fill="none" stroke="var(--white)" stroke-width="3"/>
  </svg>
  <ul class="contact">
    <li>
      <svg class="contact__icon" viewBox="0 0 30 30" aria-hidden="true"><circle cx="15" cy="15" r="15" fill="var(--white)"/><path d="M10 8 L13 8 L14 12 L12 13.5 C13 16 14 17 16.5 18 L18 16 L22 17 L22 20 C16 21 9 14 10 8 Z" fill="var(--maroon)"/></svg>
      <span>0400 555 218</span>
    </li>
    <li>
      <svg class="contact__icon" viewBox="0 0 30 30" aria-hidden="true"><circle cx="15" cy="15" r="15" fill="var(--white)"/><rect x="8" y="10" width="14" height="10" fill="var(--maroon)"/><path d="M8 10 L15 16 L22 10" fill="none" stroke="var(--white)" stroke-width="1.4"/></svg>
      <span>malcolm.darby@mailbox.com</span>
    </li>
    <li>
      <svg class="contact__icon" viewBox="0 0 30 30" aria-hidden="true"><circle cx="15" cy="15" r="15" fill="var(--white)"/><path d="M7 15 L15 8 L23 15 L21 15 L21 22 L9 22 L9 15 Z" fill="var(--maroon)"/></svg>
      <span>PO Box 1234, Riverton Mail Centre<br>QLD 4700</span>
    </li>
    <li class="contact__text--abn"><span><span class="contact__label">ABN</span> 12 345 678 901</span></li>
  </ul>
</section>

</body>
</html>
```